Rest. Build. Thrive. Book Cover

I would like a book cover for the print edition book I am self publishing. My cover will require front, back, and spine design. I have provided a template to assist with sizing and spacing.

My book is named "Rest. Build. Thrive. A Hands-On Diet, Drive to Act, and Attitude Handbook Building Energy Toward Stronger Vitality and Balance" by Gregory Halvorsen RD, CPT. I use the concept of waves as an analogy for forward progress in life and would like that reflected in the cover design. I would like the color scheme to be blacks, whites, grey, and various shades of blue. I have provided a style guide for reference. Please include my logo on the front, spine, and back of the design. Please include an about the author, book summary, and my picture on the back. I have provided the wording below.

About the Author: Gregory Halvorsen is a Registered Dietitian and Certified Personal Trainer from Cleveland, OH. He graduated from the Westbrook Valley University and currently works as a health coach in the healthcare industry. His passions are fitness, nutrition, science, and motivation. He has extensive knowledge and experience in wellness, healthcare, and disease treatment and disease. Gregory has worked with hundreds of people through counseling, consulting, and coaching in an effort to make a difference in their long-term health. In his spare time, he enjoys exercising, watching movies, and trying out new foods.

Book Summary: Believe in you. Trust in You. Rest. Build. Thrive. is a book committed to you. Behavior change and improved health can be challenging. You must feel empowered to make decisions and changes create momentum in the right direction. But, you may not always have the knowledge to do that. This book provides you with practical and fun tools and tips to improve your nutrition, motivation to move, and mindset. You are awesome. You are beautiful. You have the power to control your destiny and future. All you have to do is Rest, Build, and Thrive!

Please use a modern/ futuristic font style for the title. I have also provided some draft book covers for inspiration/ direction. Thank you!

Colors

Designer to choose only greyscale colors for use in the design.

Requirements
Must have
• Color scheme, about author, profile picture, and book summary on back, wave themed graphics

```html
<!DOCTYPE html>
<html lang="en">
<head>
<meta charset="utf-8">
<title>Rest. Build. Thrive. – Book Cover</title>
<link href="https://fonts.googleapis.com/css2?family=Dosis:wght@300;400;600;700&display=swap" rel="stylesheet">
<style>
  :root {
    --page: #ececec;
    --cover-deep: #17222e;
    --cover-mid: #24323f;
    --cover-top: #2f3d4b;
    --ice: #e4fbff;
    --ink: #16202a;
    --text-light: #eef3f7;
    --logo-blue: #6b9fd0;
    --photo-dark: #2a2f35;
    --photo-light: #9a9fa5;
    --night: #1b2631;
    --trail: #e9edf0;
  }
  * { box-sizing: border-box; margin: 0; padding: 0; }
  html, body { width: 1200px; height: 946px; overflow: hidden; }
  body { background: var(--page); font-family: "Dosis", sans-serif; position: relative; }

  .cover {
    position: absolute; left: 94px; top: 94px; width: 1012px; height: 756px;
    background: linear-gradient(165deg, var(--cover-top) 0%, var(--cover-deep) 50%, var(--cover-mid) 100%);
    box-shadow: 6px 6px 10px rgba(0,0,0,0.45);
    overflow: hidden;
  }

  /* back cover */
  .back { position: absolute; left: 0; top: 0; width: 474px; height: 756px; color: var(--text-light); }
  .heading { position: absolute; left: 0; width: 474px; text-align: center; font-weight: 400; font-size: 18px; letter-spacing: 0.2px; }
  .summary-heading { top: 47px; }
  .author-heading { top: 482px; }
  .body-copy { position: absolute; text-align: center; font-weight: 300; font-size: 12.6px; line-height: 15.8px; }
  .summary-copy { left: 42px; width: 390px; top: 76px; }
  .author-copy { left: 38px; width: 398px; top: 505px; }
  .author-photo {
    position: absolute; left: 44px; top: 189px; width: 386px; height: 287px;
    background: linear-gradient(110deg, var(--photo-dark) 0%, #6b7077 45%, var(--photo-light) 100%);
  }
  .code-box { position: absolute; left: 308px; top: 648px; width: 129px; height: 82px; background: #fff; }

  /* night road area shared by spine and front */
  .road-photo {
    position: absolute; left: 474px; top: 186px; width: 538px; height: 394px;
    background:
      radial-gradient(ellipse 60% 12% at 62% 74%, rgba(240,244,247,0.85), rgba(240,244,247,0) 100%),
      linear-gradient(174deg, var(--night) 0%, #222e3a 40%, #3b4753 62%, #8d979f 71%, var(--trail) 75%, #7f8992 80%, #323d48 90%, #1f2a35 100%);
  }
  .wave-lines { position: absolute; left: 474px; top: 186px; width: 538px; height: 394px; }

  /* spine */
  .spine {
    position: absolute; left: 474px; top: 0; width: 64px; height: 756px;
    border-left: 1px solid #55677a; border-right: 1px solid #55677a;
  }
  .spine-logo-block { position: absolute; left: 0; top: 0; width: 62px; height: 234px; background: linear-gradient(180deg, #2e3e4e, #3a4e62); }
  .spine-logo {
    position: absolute; left: 22px; top: 70px; writing-mode: vertical-rl;
    color: var(--logo-blue); font-weight: 700; font-size: 14px; letter-spacing: 1px;
  }
  .spine-author {
    position: absolute; left: 13px; top: 630px; writing-mode: vertical-rl;
    color: var(--text-light); font-weight: 600; font-size: 13.5px; line-height: 18px;
  }

  /* front cover */
  .front { position: absolute; left: 538px; top: 0; width: 474px; height: 756px; }
  .front-logo {
    position: absolute; left: 0; top: 52px; width: 474px; text-align: center;
    color: var(--logo-blue); font-weight: 700; font-size: 30px; line-height: 29px; letter-spacing: 2px;
  }
  .ice-rule { position: absolute; left: 0; top: 180px; width: 474px; height: 6px; background: var(--ice); }
  .name-band { position: absolute; left: 474px; top: 580px; width: 538px; height: 37px; background: var(--ice); }
  .author-name {
    position: absolute; left: 0; top: 580px; width: 474px; line-height: 37px; text-align: center;
    color: var(--ink); font-weight: 600; font-size: 24px;
  }
  .subtitle {
    position: absolute; left: 57px; top: 655px; width: 360px; text-align: center;
    color: var(--text-light); font-weight: 600; font-size: 13.4px; line-height: 17.6px;
  }
</style>
</head>
<body>
  <div class="cover">
    <section class="back">
      <h2 class="heading summary-heading">BOOK SUMMARY:</h2>
      <p class="body-copy summary-copy">Believe in you. Trust in You. Rest. Build. Thrive. is a book committed to you. You must feel empowered to make decisions and changes to improve your life and health. But, you may not always have the knowledge to do that. This book provides you with practical and fun tools and tips to improve your fitness level, healthy eating, and mental strength. You are awesome. You are beautiful. You have the power to control your destiny and future. All you have to do is Rest, Build, and Thrive!</p>
      <div class="author-photo" role="img" aria-label="Black and white portrait of the author smiling in a kitchen"></div>
      <h2 class="heading author-heading">ABOUT THE AUTHOR:</h2>
      <p class="body-copy author-copy">Gregory Halvorsen is a Registered Dietitian and Certified Personal Trainer from Cleveland, OH. He graduated from the Westbrook Valley University and currently works as a health coach in the healthcare industry. His passions are fitness, nutrition, science, and motivation. He has extensive knowledge and experience in wellness, healthcare, and disease treatment and disease. Gregory has worked with hundreds of people through counseling, consulting, and coaching in an effort to make a difference in their long-term health. In his spare time, he enjoys exercising, watching movies, and trying out new foods.</p>
      <div class="code-box"></div>
    </section>

    <div class="road-photo" role="img" aria-label="Night city road under an overpass with street lights and bright light trails"></div>
    <svg class="wave-lines" viewBox="0 0 538 394" aria-hidden="true">
      <g fill="none" stroke="#f2f6f9" stroke-linecap="round">
        <path d="M0 300 C 90 270, 170 310, 270 285 S 450 255, 538 262" stroke-width="1.6" opacity="0.55"/>
        <path d="M0 318 C 100 292, 190 330, 290 300 S 460 272, 538 278" stroke-width="2.4" opacity="0.7"/>
        <path d="M0 336 C 110 312, 200 348, 300 318 S 470 290, 538 296" stroke-width="1.4" opacity="0.5"/>
        <path d="M0 352 C 120 332, 210 362, 310 336 S 480 310, 538 314" stroke-width="1" opacity="0.35"/>
      </g>
    </svg>

    <section class="spine">
      <div class="spine-logo-block"></div>
      <div class="spine-logo">REST BUILD THRIVE</div>
      <div class="spine-author">Gregory<br>Halvorsen RD, CPT</div>
    </section>

    <div class="name-band"></div>

    <section class="front">
      <div class="front-logo">REST<br>BUILD<br>THRIVE</div>
      <div class="ice-rule"></div>
      <h1 class="author-name">Gregory Halvorsen RD, CPT</h1>
      <p class="subtitle">REST. BUILD. THRIVE:<br>A Hands-On Diet, Drive to Act, and Attitude Handbook Building Energy Toward Stronger Vitality and Balance</p>
    </section>
  </div>
</body>
</html>
```